Home care support

Design a a great and dynamic website for a healthcare business. Our business will be involved in providing care at home for people with disability and the elderly. Below is a link that I found for a company offering similar services in the US. I am looking for something like this .
I have my files - the latest project in here in through through PixelNest
Sample site : https://pinegroveattendants.net/
Target Market(s)
people with disability and elderly seniors who need home care support
Industry/Entity Type
Health
Coding
Coded - Design and coding required
Number of Pages Required
5+ page
Requirements
Must have
- inspirational pictures and designed with the themed logo (files attached)
Nice to have
- This is my sample and should look like this : https://pinegroveattendants.net/

```html
<!DOCTYPE html>
<html lang="en">
<head>
<meta charset="utf-8">
<title>Corvale Healthcare – Home Care Support</title>
<link href="https://fonts.googleapis.com/css2?family=Poppins:wght@300;400;500;600;700&display=swap" rel="stylesheet">
<style>
:root{
  --blue:#0b6aa2;
  --blue-dark:#08598a;
  --green:#6a9a3a;
  --green-pale:#eef4e6;
  --ink:#444;
  --ink-soft:#666;
  --field:#f2f2f2;
  --rule:#e3e3e3;
  --white:#fff;
}
*{box-sizing:border-box;margin:0;padding:0}
html,body{width:1200px;height:3420px;overflow:hidden}
body{position:relative;font-family:"Poppins",sans-serif;color:var(--ink);background:var(--white)}
.abs{position:absolute}
svg{display:block}

/* top bar */
.topbar{top:0;left:0;width:1200px;height:30px;background:var(--blue);color:var(--white);font-size:13px}
.topbar .item{top:7px;display:flex;align-items:center;gap:7px}
.topbar .sep{top:0;width:1px;height:30px;background:rgba(255,255,255,.25)}
.topbar .sq{top:9px;width:12px;height:12px;border-radius:2px;background:var(--white)}

/* header */
.brand{display:flex;align-items:center;gap:10px}
.brand .dot{border-radius:50%}
.brand .name{font-weight:600;letter-spacing:1px}
.header-brand{top:56px;left:89px}
.header-brand .dot{width:50px;height:50px;border:5px solid var(--blue)}
.header-brand .name{font-size:30px;color:var(--blue)}
.nav{top:74px;left:535px;display:flex;gap:26px;font-size:12px;font-weight:500;color:#333}
.nav .active{color:var(--green);position:relative}
.nav .active:after{content:"";position:absolute;left:8px;right:8px;bottom:-8px;height:3px;border-radius:2px;background:var(--green)}

/* hero */
.hero-title{top:226px;left:89px;font-size:58px;line-height:58px;font-weight:600;color:#4a4a4a}
.hero-rule{top:258px;left:303px;width:189px;height:2px;background:#ddd}
.hero-sub{top:425px;left:89px;font-size:24px;color:#444}
.hero-text{top:474px;left:89px;width:420px;font-size:15px;line-height:22px;color:var(--ink-soft)}
.btn{display:flex;align-items:center;justify-content:center;border-radius:22px;font-weight:600;text-transform:uppercase;font-size:11px}
.btn-green{background:var(--green);color:var(--white)}
.hero-btn{top:544px;left:89px;width:187px;height:39px}
.hero-call{top:556px;left:294px;font-size:11px;font-weight:600;color:#333}

/* features */
.feature{width:300px;height:120px}
.feature .ic{top:0;left:0;width:80px;height:80px;border-radius:50%;background:var(--white);box-shadow:0 4px 10px rgba(11,106,162,.12);display:flex;align-items:center;justify-content:center}
.feature h4{position:absolute;top:0;left:97px;font-size:15px;font-weight:500;color:#333}
.feature p{position:absolute;top:28px;left:97px;width:180px;font-size:13.5px;line-height:20px;color:var(--ink-soft)}
.feature-rule{top:872px;width:165px;height:1px;background:var(--rule)}

/* approach band */
.band-pale{top:1079px;left:0;width:1138px;height:531px;background:var(--green-pale);border-radius:0 440px 440px 0/0 270px 270px 0}
.band{top:1079px;left:0;width:1110px;height:531px;background:var(--green);border-radius:0 420px 420px 0/0 270px 270px 0}
.band h2{position:absolute;top:88px;left:561px;width:400px;font-size:33px;line-height:36px;font-weight:500;color:var(--white)}
.band .rule{position:absolute;top:205px;left:561px;width:50px;height:2px;background:rgba(255,255,255,.5)}
.band p{position:absolute;top:225px;left:561px;width:430px;font-size:14.5px;line-height:23px;color:var(--white)}
.band .btn{position:absolute;top:405px;left:561px;width:134px;height:39px;background:rgba(255,255,255,.25);color:var(--white)}

/* services */
.section-title{font-size:34px;font-weight:500;color:#444;text-align:center}
.services-title{top:1692px;left:0;width:1200px}
.title-rule{height:2px;width:50px;background:var(--rule)}
.service h4{font-size:15px;font-weight:500;color:#333}
.service p{font-size:13.5px;line-height:18px;color:var(--ink-soft);margin-top:3px}
.service.left{text-align:right;width:240px}
.service.right{width:240px}
.service-ic{width:48px;height:48px}
.center-mark{top:1768px;left:470px;width:260px;height:260px}
.services-btn{top:2073px;left:519px;width:161px;height:38px}
.section-rule{top:2188px;left:89px;width:1020px;height:1px;background:var(--rule)}

/* contact */
.contact-title{top:2242px;left:153px;font-size:32px;font-weight:500;color:#444}
.contact-rule{top:2300px;left:153px;width:50px;height:2px;background:var(--rule)}
.label{font-size:11px;font-weight:600;color:#333;text-transform:uppercase}
.field{background:var(--field);font-size:12px;color:#777;padding:0 14px;display:flex;align-items:center}
.send-btn{top:2634px;left:294px;width:127px;height:40px}

/* cta */
.cta{top:2796px;left:212px;width:776px;height:207px;border-radius:104px;background:var(--green);text-align:center;color:var(--white);box-shadow:0 10px 24px rgba(0,0,0,.12)}
.cta h2{margin-top:40px;font-size:31px;font-weight:500}
.cta p{margin-top:2px;font-size:17px}
.cta .btn{margin:14px auto 0;width:204px;height:41px;background:var(--white);color:#333}

/* footer */
.footer-text{color:var(--white)}
.footer-brand{top:3146px;left:89px}
.footer-brand .dot{width:64px;height:64px;border:5px solid var(--white)}
.footer-brand .name{font-size:40px;color:var(--white)}
.social{top:3225px;left:117px;display:flex;gap:11px}
.social span{width:41px;height:41px;border-radius:50%;background:rgba(255,255,255,.15)}
.f-col h4{font-size:19px;font-weight:600;color:var(--white);margin-bottom:14px}
.f-links li{list-style:none;font-size:13px;color:var(--white);line-height:31px}
.f-links li:before{content:"›";margin-right:8px}
.f-contact .row{display:flex;gap:8px;font-size:13px;line-height:18px;color:var(--white);margin-bottom:12px}
.newsletter p{font-size:13px;line-height:18px;color:var(--white);width:230px}
.news-field{margin-top:20px;width:260px;height:46px;border-radius:23px;background:var(--white);display:flex;align-items:center;padding:0 14px 0 20px;font-size:12.5px;color:#888;gap:10px}
.bottom-rule{top:3356px;left:0;width:1200px;height:1px;background:rgba(255,255,255,.25)}
.copyright{top:3380px;left:89px;font-size:13px;color:var(--white)}
.legal{top:3380px;right:89px;display:flex;gap:26px;font-size:13px;color:var(--white)}
.to-top{top:3336px;left:1130px;width:42px;height:42px;border-radius:50%;background:var(--green);display:flex;align-items:center;justify-content:center}
</style>
</head>
<body>

<!-- top bar -->
<div class="abs topbar">
  <div class="abs item" style="left:89px">
    <svg width="12" height="12" viewBox="0 0 24 24"><path fill="#fff" d="M6.6 10.8a15 15 0 0 0 6.6 6.6l2.2-2.2c.3-.3.7-.4 1-.2 1.1.4 2.3.6 3.6.6.6 0 1 .4 1 1V20c0 .6-.4 1-1 1A17 17 0 0 1 3 4c0-.6.4-1 1-1h3.5c.6 0 1 .4 1 1 0 1.3.2 2.5.6 3.6.1.3 0 .7-.2 1z"/></svg>
    (555) 014-2270
  </div>
  <div class="abs sep" style="left:223px"></div>
  <div class="abs item" style="left:250px">
    <svg width="13" height="10" viewBox="0 0 26 20"><rect width="26" height="20" rx="2" fill="#fff"/><path d="M1 2l12 9 12-9" stroke="#0b6aa2" stroke-width="2" fill="none"/></svg>
    contact@corvalehealthcare.com
  </div>
  <div class="abs sep" style="left:978px"></div>
  <div class="abs sq" style="left:996px"></div>
  <div class="abs sep" style="left:1025px"></div>
  <div class="abs sq" style="left:1044px;border-radius:50%"></div>
  <div class="abs sep" style="left:1075px"></div>
  <div class="abs sq" style="left:1096px;border-radius:50%"></div>
</div>

<!-- header -->
<div class="abs brand header-brand"><span class="dot"></span><span class="name">CORVALE</span></div>
<nav class="abs nav">
  <span class="active">HOME</span><span>ABOUT</span><span>SERVICES</span><span>FAQ</span><span>RESOURCES ⌄</span><span>EMPLOYMENT</span><span>CONTACT</span>
</nav>
<svg class="abs" style="top:75px;left:1095px" width="15" height="15" viewBox="0 0 16 16"><circle cx="6.5" cy="6.5" r="5" stroke="#333" stroke-width="1.8" fill="none"/><path d="M10.5 10.5l4 4" stroke="#333" stroke-width="1.8"/></svg>

<!-- hero -->
<h1 class="abs hero-title">We are<br>committed to<br>your well being</h1>
<div class="abs hero-rule"></div>
<div class="abs hero-sub">The Best Care is Corvale healthcare</div>
<p class="abs hero-text">Aenean sollicitudin lorem quis bibendum auctor nisi elit vulputate cursus sit amet mauris morbi accumsan...</p>
<a class="abs btn btn-green hero-btn">Make an appointment</a>
<div class="abs hero-call">CALL US:&nbsp; (555) 014-2270</div>

<svg class="abs" style="top:100px;left:620px" width="580" height="600" viewBox="0 0 580 600">
  <circle cx="300" cy="288" r="300" fill="var(--blue)"/>
  <circle cx="322" cy="262" r="282" fill="#fff"/>
  <path d="M520 60 A282 282 0 0 1 580 140 L580 180 A300 300 0 0 0 510 68 Z" fill="var(--blue)"/>
  <defs><linearGradient id="heroPhoto" x1="0" y1="0" x2="1" y2="1"><stop offset="0" stop-color="#d9d6d2"/><stop offset=".55" stop-color="#8a98a8"/><stop offset="1" stop-color="#3c3f45"/></linearGradient></defs>
  <circle cx="312" cy="258" r="242" fill="url(#heroPhoto)" role="img" aria-label="Photo: a carer helping an elderly woman walk with a frame at home"/>
</svg>

<!-- features -->
<div class="abs feature" style="top:764px;left:143px">
  <div class="abs ic"><svg width="40" height="40" viewBox="0 0 40 40" fill="none" stroke="var(--blue)" stroke-width="2"><circle cx="18" cy="7" r="3"/><path d="M18 11v12h9l4 9M18 16h8"/><path d="M13 19a9 9 0 1 0 12 11"/></svg></div>
  <h4>Choice of Caregiver</h4><p>Bibendum auctor nisi elit vulputate cursus sit.</p>
</div>
<div class="abs feature" style="top:764px;left:467px">
  <div class="abs ic"><svg width="40" height="40" viewBox="0 0 40 40" fill="none" stroke="var(--blue)" stroke-width="2"><circle cx="17" cy="13" r="7"/><path d="M4 34c1-8 6-12 13-12s12 4 13 12z"/><circle cx="28" cy="10" r="5"/></svg></div>
  <h4>Friendly Staff</h4><p>Bibendum auctor nisi elit vulputate cursus sit.</p>
</div>
<div class="abs feature" style="top:764px;left:791px">
  <div class="abs ic"><svg width="40" height="40" viewBox="0 0 40 40" fill="none" stroke="var(--blue)" stroke-width="2"><path d="M10 6l6 6-3 4a18 18 0 0 0 11 11l4-3 6 6-4 4C18 34 6 22 6 10z"/><circle cx="26" cy="14" r="8"/><path d="M26 9v5h4"/></svg></div>
  <h4>On Call 24/7</h4><p>Bibendum auctor nisi elit vulputate cursus sit.</p>
</div>
<div class="abs feature-rule" style="left:240px"></div>
<div class="abs feature-rule" style="left:564px"></div>
<div class="abs feature-rule" style="left:888px"></div>
<div class="abs feature" style="top:915px;left:143px">
  <div class="abs ic"><svg width="40" height="40" viewBox="0 0 40 40" fill="none" stroke="var(--blue)" stroke-width="2"><rect x="4" y="8" width="28" height="24" rx="2"/><path d="M4 15h28M11 4v7M25 4v7M9 20h4M16 20h4M23 20h4M9 26h4M16 26h4"/><circle cx="30" cy="30" r="6" fill="#fff"/><path d="M30 27v3h3"/></svg></div>
  <h4>Flexible Schedule</h4><p>Bibendum auctor nisi elit vulputate cursus sit.</p>
</div>
<div class="abs feature" style="top:915px;left:467px">
  <div class="abs ic"><svg width="40" height="40" viewBox="0 0 40 40" fill="none" stroke="var(--blue)" stroke-width="2"><path d="M4 19L20 6l16 13M9 16v17h22V16"/><circle cx="20" cy="24" r="6"/><path d="M20 20v8"/></svg></div>
  <h4>Home Assessments</h4><p>Bibendum auctor nisi elit vulputate cursus sit.</p>
</div>
<div class="abs feature" style="top:915px;left:791px">
  <div class="abs ic"><svg width="40" height="40" viewBox="0 0 40 40" fill="none" stroke="var(--blue)" stroke-width="2"><path d="M12 36v-7c-4-3-6-7-6-12A13 13 0 0 1 32 15l3 7h-3v6h-6v8"/><circle cx="19" cy="16" r="6"/><path d="M19 10v12M19 16l-4 4M19 16l4 4"/></svg></div>
  <h4>Peace of Mind</h4><p>Bibendum auctor nisi elit vulputate cursus sit.</p>
</div>

<!-- approach band -->
<div class="abs band-pale"></div>
<section class="abs band">
  <svg class="abs" style="top:0;left:0" width="520" height="531" viewBox="0 0 520 531">
    <circle cx="290" cy="252" r="206" fill="#fff"/>
    <circle cx="276" cy="232" r="202" fill="var(--green)"/>
    <defs><linearGradient id="bandPhoto" x1="0" y1="0" x2="1" y2="1"><stop offset="0" stop-color="#f0ebe4"/><stop offset=".45" stop-color="#e6dc6a"/><stop offset="1" stop-color="#6f7b80"/></linearGradient></defs>
    <circle cx="297" cy="219" r="172" fill="url(#bandPhoto)" role="img" aria-label="Photo: a smiling carer talking with an elderly woman in a wheelchair"/>
  </svg>
  <h2>A simple, affordable approach to corvale healthcare</h2>
  <div class="rule"></div>
  <p>Aenean sollicitudin, lorem quis bibendum auctor, nisi elit consequat ipsum, nec sagittis sem nibh id elit. Duis sed odio sit amet nibh vulputate cursus a sit amet mauris. Morbi accumsan ipsum velit. nam nec tellus a odio tincidunt auctor a ornare odio. Sed non&nbsp; mauris vitae erat consequat auctor eu in elit. Class aptent taciti sociosqu ad litora torquent per conubia nostra...</p>
  <a class="btn">Find out more</a>
</section>

<!-- services -->
<h2 class="abs section-title services-title">Corvale healthcare Services</h2>
<div class="abs title-rule" style="top:1746px;left:575px"></div>

<div class="abs service left" style="top:1778px;left:133px"><h4>Companion Care</h4><p>Bibendum auctor nisi elit<br>vulputate cursus sit.</p></div>
<div class="abs service left" style="top:1882px;left:133px"><h4>Transportation</h4><p>Bibendum auctor nisi elit<br>vulputate cursus sit.</p></div>
<div class="abs service left" style="top:1983px;left:133px"><h4>Shopping &amp; Errands</h4><p>Bibendum auctor nisi elit<br>vulputate cursus sit.</p></div>
<svg class="abs service-ic" style="top:1780px;left:390px" viewBox="0 0 48 48" fill="none" stroke="var(--blue)" stroke-width="2"><path d="M24 24s-9-6-9-11a5 5 0 0 1 9-2 5 5 0 0 1 9 2c0 5-9 11-9 11z"/><path d="M4 34l8-6h12l-4 4h-6M12 28l-8 12M20 32h10l12-8-4 12-18 6"/></svg>
<svg class="abs service-ic" style="top:1884px;left:390px" viewBox="0 0 48 48" fill="none" stroke="var(--blue)" stroke-width="2"><circle cx="18" cy="12" r="8"/><path d="M18 8v4h3"/><path d="M6 36V24h26v12M32 28h8l4 6v2H32"/><circle cx="13" cy="38" r="3"/><circle cx="36" cy="38" r="3"/></svg>
<svg class="abs service-ic" style="top:1984px;left:390px" viewBox="0 0 48 48" fill="none" stroke="var(--blue)" stroke-width="2"><circle cx="26" cy="20" r="16"/><path d="M10 20h32M26 4c-6 6-6 26 0 32M26 4c6 6 6 26 0 32"/><path d="M2 30h4l4 12h14l3-9H8"/><circle cx="12" cy="45" r="1.5"/><circle cx="22" cy="45" r="1.5"/></svg>

<svg class="abs center-mark" viewBox="0 0 260 260">
  <circle cx="130" cy="130" r="126" fill="none" stroke="var(--blue)" stroke-width="7"/>
  <circle cx="130" cy="130" r="108" fill="var(--green)"/>
  <text x="130" y="141" text-anchor="middle" font-family="Poppins, sans-serif" font-size="30" font-weight="600" fill="#fff" letter-spacing="1">CORVALE</text>
</svg>

<svg class="abs service-ic" style="top:1780px;left:762px" viewBox="0 0 48 48" fill="none" stroke="var(--blue)" stroke-width="2"><path d="M4 22L22 6l18 16M9 18v24h26V18"/><rect x="16" y="28" width="8" height="14"/><path d="M36 30v12h8V30l-4-4z"/><circle cx="22" cy="18" r="3"/></svg>
<svg class="abs service-ic" style="top:1884px;left:762px" viewBox="0 0 48 48" fill="none" stroke="var(--blue)" stroke-width="2"><path d="M17 32c0-4-5-7-5-14a12 12 0 0 1 24 0c0 7-5 10-5 14z"/><path d="M18 37h12M20 42h8M26 12l-5 9h6l-4 8"/><path d="M24 2v3M6 18H3M45 18h-3M10 6l2 2M38 6l-2 2"/></svg>
<svg class="abs service-ic" style="top:1984px;left:762px" viewBox="0 0 48 48" fill="none" stroke="var(--blue)" stroke-width="2"><path d="M30 4H10v40h26V22"/><path d="M30 4v8h6M15 16h12M15 22h14M15 28h10M15 34h6"/><path d="M42 12L26 34l-4 2 1-4 16-22z"/></svg>

<div class="abs service right" style="top:1778px;left:821px"><h4>Light Housekeeping</h4><p>Bibendum auctor nisi elit<br>vulputate cursus sit.</p></div>
<div class="abs service right" style="top:1882px;left:821px"><h4>Stimulating Activities</h4><p>Bibendum auctor nisi elit<br>vulputate cursus sit.</p></div>
<div class="abs service right" style="top:1983px;left:821px"><h4>Correspondence</h4><p>Bibendum auctor nisi elit<br>vulputate cursus sit.</p></div>

<a class="abs btn btn-green services-btn">View all services</a>
<div class="abs section-rule"></div>

<!-- contact -->
<h2 class="abs contact-title">Get in touch with us</h2>
<div class="abs contact-rule"></div>
<form>
  <div class="abs label" style="top:2322px;left:153px">Name*</div>
  <div class="abs label" style="top:2322px;left:360px">Email*</div>
  <div class="abs field" style="top:2341px;left:157px;width:196px;height:40px">Enter your name</div>
  <div class="abs field" style="top:2341px;left:360px;width:197px;height:40px">Enter your email</div>
  <div class="abs label" style="top:2396px;left:153px">Phone*</div>
  <div class="abs label" style="top:2396px;left:360px">Date*</div>
  <div class="abs field" style="top:2415px;left:157px;width:196px;height:40px">Enter phone number</div>
  <div class="abs field" style="top:2415px;left:360px;width:197px;height:40px;justify-content:space-between">Select date <span>⌄</span></div>
  <div class="abs label" style="top:2476px;left:153px">Phone*</div>
  <div class="abs field" style="top:2495px;left:157px;width:401px;height:113px;align-items:flex-start;padding-top:16px">Type your text...</div>
  <a class="abs btn btn-green send-btn">Send now</a>
</form>
<svg class="abs" style="top:2255px;left:620px" width="430" height="420" viewBox="0 0 430 420">
  <circle cx="212" cy="205" r="207" fill="var(--blue)"/>
  <circle cx="216" cy="186" r="194" fill="#fff"/>
  <defs><linearGradient id="contactPhoto" x1="0" y1="0" x2="1" y2="1"><stop offset="0" stop-color="#e4e2e0"/><stop offset=".5" stop-color="#8d9aa8"/><stop offset="1" stop-color="#2f3a4e"/></linearGradient></defs>
  <circle cx="212" cy="180" r="171" fill="url(#contactPhoto)" role="img" aria-label="Photo: a carer supporting an elderly man seated in a wheelchair"/>
</svg>

<!-- footer -->
<svg class="abs" style="top:2900px;left:0" width="1200" height="520" viewBox="0 0 1200 520">
  <path d="M0 160 Q600 -210 1200 140 L1200 520 L0 520 Z" fill="#e4eef5"/>
  <path d="M0 190 Q600 -170 1200 170 L1200 520 L0 520 Z" fill="var(--blue)"/>
</svg>

<section class="abs cta">
  <h2>Better corvale healthcare is our mission</h2>
  <p>24/7 service. flexible appointments and care options</p>
  <a class="btn">Make an appointment</a>
</section>

<div class="abs brand footer-brand"><span class="dot"></span><span class="name">CORVALE</span></div>
<div class="abs social"><span></span><span></span><span></span><span></span></div>

<div class="abs f-col" style="top:3078px;left:418px">
  <h4>Quick links</h4>
  <ul class="f-links"><li>About Us</li><li>Services</li><li>FAQ</li><li>Resources</li><li>Employment</li><li>Contact</li></ul>
</div>
<div class="abs f-col f-contact" style="top:3078px;left:602px">
  <h4>Contact info</h4>
  <div class="row"><svg width="13" height="10" viewBox="0 0 26 20" style="margin-top:4px"><rect width="26" height="20" rx="2" fill="#fff"/><path d="M1 2l12 9 12-9" stroke="#0b6aa2" stroke-width="2" fill="none"/></svg><span>Email:<br>info@corvalecare.net</span></div>
  <div class="row"><svg width="13" height="13" viewBox="0 0 24 24" style="margin-top:3px"><path fill="#fff" d="M6.6 10.8a15 15 0 0 0 6.6 6.6l2.2-2.2c.3-.3.7-.4 1-.2 1.1.4 2.3.6 3.6.6.6 0 1 .4 1 1V20c0 .6-.4 1-1 1A17 17 0 0 1 3 4c0-.6.4-1 1-1h3.5c.6 0 1 .4 1 1 0 1.3.2 2.5.6 3.6.1.3 0 .7-.2 1z"/></svg><span>Phone:<br>+44 20 7946 0321</span></div>
  <div class="row"><svg width="11" height="14" viewBox="0 0 12 16" style="margin-top:3px"><path fill="#fff" d="M6 0a6 6 0 0 0-6 6c0 4.5 6 10 6 10s6-5.5 6-10a6 6 0 0 0-6-6zm0 8.5A2.5 2.5 0 1 1 6 3.5a2.5 2.5 0 0 1 0 5z"/></svg><span>Location:<br>Some address line here<br>United Kingdom ZX9 4QT</span></div>
</div>
<div class="abs f-col newsletter" style="top:3080px;left:851px">
  <h4>Newsletter</h4>
  <p>Subscribe to our email address to get the latest news.</p>
  <div class="news-field">
    <svg width="13" height="10" viewBox="0 0 26 20"><rect width="26" height="20" rx="2" fill="#bbb"/><path d="M1 2l12 9 12-9" stroke="#fff" stroke-width="2" fill="none"/></svg>
    <span style="flex:1">Enter your email...</span>
    <svg width="16" height="16" viewBox="0 0 24 24"><path fill="var(--green)" d="M22 2L2 10l7 3 2 7 3-5 5 4z"/></svg>
  </div>
</div>

<div class="abs bottom-rule"></div>
<div class="abs copyright">© Copyright 2022 Corvale Healthcare. All Rights Reserved</div>
<div class="abs legal"><span>Imprint</span><span>Privacy policy</span><span>Terms and Condition</span></div>
<div class="abs to-top"><svg width="14" height="16" viewBox="0 0 14 16" fill="none" stroke="#fff" stroke-width="1.6"><path d="M7 15V2M2 7l5-5 5 5"/></svg></div>

</body>
</html>
```